Flyer promoting Veltrane's workshops and credentials

We run Training workshops for the data analyst community. We'd like a flyer to sell our services using a style and colour scheme consistent with our website www.veltranepartners.co.uk . I've attached some background info and some existing e-brochures for different workshops to give a flavour for content (but these are poorly designed and we don't want a similar design!!). There's also an overview document which gives more direction. The flyer will be sent with an accompanying letter to Learning & Development decision makers as well as Anlaytical team managers. It's purpose would be to generate enquiries and bookings for primarliy our flagship workshop 'Turning Figures Into Real Gains'.

Target Market(s)

Learning and Development senior managers
Analytical team managers

Industry/Entity Type

Training

Other font styles liked:
• Similar to website for consistency

Requirements
Must have
• Good copy! Slick design more in line with European (UK) style advertising rather than US.
Nice to have
• Some humour,
Should not have
• should not be as boring and non-sales based as the website!! Website is not a great example!

```html
<!DOCTYPE html>
<html lang="en">
<head>
<meta charset="utf-8">
<title>Veltrane – Turning Figures Into Real Gains</title>
<link rel="stylesheet" href="https://fonts.googleapis.com/css2?family=PT+Sans:wght@400;700&family=Roboto+Condensed:wght@700&display=swap">
<style>
  :root {
    --page: #ffffff;
    --ink: #1c1c1c;
    --brand-blue: #2a4a8c;
    --title-blue: #2f4f8f;
    --accent-orange: #f28a12;
    --band: #cfd2e3;
  }
  * { margin: 0; padding: 0; box-sizing: border-box; }
  html, body { width: 900px; height: 1200px; overflow: hidden; background: var(--page); }
  .flyer {
    position: relative;
    width: 900px;
    height: 1200px;
    background: var(--page);
    font-family: "PT Sans", sans-serif;
    color: var(--ink);
  }
  .brand {
    position: absolute;
    left: 46px;
    top: 40px;
  }
  .brand-name {
    font-weight: 700;
    font-size: 52px;
    line-height: 1;
    color: var(--brand-blue);
  }
  .brand-tagline {
    font-weight: 700;
    font-size: 17px;
    color: var(--accent-orange);
    margin-top: 2px;
    margin-left: 4px;
  }
  .contact {
    position: absolute;
    left: 600px;
    top: 58px;
    font-weight: 700;
    font-size: 15px;
    line-height: 21px;
    color: var(--accent-orange);
  }
  .headline {
    position: absolute;
    left: 92px;
    top: 172px;
    width: 682px;
    height: 60px;
    background: var(--title-blue);
    border: 3px solid var(--accent-orange);
    display: flex;
    align-items: center;
    justify-content: center;
    font-family: "Roboto Condensed", sans-serif;
    font-weight: 700;
    font-size: 35px;
    color: #ffffff;
  }
  .intro {
    position: absolute;
    left: 100px;
    top: 268px;
    width: 722px;
    font-size: 18px;
    line-height: 25.5px;
    text-align: justify;
  }
  .lead-in {
    position: absolute;
    left: 100px;
    top: 528px;
    font-size: 18px;
    font-weight: 700;
  }
  .challenges {
    position: absolute;
    left: 100px;
    top: 572px;
    width: 712px;
    list-style: none;
    font-size: 18px;
    line-height: 26px;
  }
  .challenges li { padding-left: 26px; text-indent: -26px; }
  .divider {
    position: absolute;
    left: 0;
    top: 956px;
    width: 900px;
    height: 18px;
    background: var(--accent-orange);
  }
  .footer-band {
    position: absolute;
    left: 0;
    top: 974px;
    width: 900px;
    height: 226px;
    background: var(--band);
  }
  .footer-copy {
    position: absolute;
    left: 82px;
    top: 1006px;
    width: 744px;
    font-size: 14.6px;
    line-height: 20px;
    text-align: justify;
  }
  .footer-copy strong { font-weight: 700; }
</style>
</head>
<body>
<main class="flyer">
  <header>
    <div class="brand">
      <div class="brand-name">Veltrane</div>
      <div class="brand-tagline">Workshops for Data Analysts</div>
    </div>
    <div class="contact">
      <div>Web: www.veltranepartners.co.uk</div>
      <div>Tel: 0161 555 0142</div>
      <div>email: info@veltranepartners.co.uk</div>
    </div>
  </header>

  <h1 class="headline">Turning Figures Into Real Gains</h1>

  <p class="intro">Our flagship two-day workshop gives analysts the practical steps and proven behaviours they need to deliver an outstanding analytical service – while raising their impact and boosting productivity by cutting out costly re-work. Whatever their level, analysts leave with a clear set of standards that builds credibility and trust with customers, and frees them to work proactively instead of fire-fighting. Every delegate takes home a checklist of behaviours and actions as an aide-mémoire, and several organisations have already built it into their personal development reviews. Why does it work? Because almost every analytical team recognises at least one of these familiar challenges.</p>

  <p class="lead-in">Sound familiar?</p>

  <ul class="challenges">
    <li>1) They take on too much work – planning slips, deadlines go un-negotiated and “yes” becomes the default answer.</li>
    <li>2) They work reactively and never find the time to add real value.</li>
    <li>3) Customers leave them out of the wider process, so they miss the full picture and get called in at the last minute.</li>
    <li>4) Briefs are vague and minds change often, which means round after round of re-work.</li>
    <li>5) Customers think it’s all “just a press of a button” – when in reality it takes far more than that.</li>
    <li>6) They struggle to be heard and have a low profile within the business.</li>
    <li>7) They spend their days turning the handle on a report machine, rather than shaping decisions.</li>
  </ul>

  <div class="divider"></div>
  <footer class="footer-band"></footer>
  <p class="footer-copy">The workshop tackles every one of these challenges through dedicated sessions on communication, planning and presenting data – and it is CPD accredited, backed by glowing testimonials from delegates and their managers. <strong>For Learning &amp; Development:</strong> CPD-accredited soft skills training built specifically for data analysts, data scientists, Management Information and Business Intelligence professionals. <strong>For Analytical Managers:</strong> complementary soft skills training that turns capable analysts into proactive, customer-focused, consultative partners. Call 0161 555 0142 or visit www.veltranepartners.co.uk to book your team’s place.</p>
</main>
</body>
</html>
```